Book Cover for Political Biography

Back round color, darker green.

This book is a political biography of Mr. Ter Haar Veldt who was a prominent politician in Curacao.

Looking for a modern toward the conservative look. The attached images can be used as place holders, we will get hi resolution ones to replace.

Book Title:
Mr. Dr. Anselm ter Haar Veldt: Pionier voor het Bestuurlijke Zelfbeschikking der Westelijke Eilanden

Name Author:
drs. K.J. (Thibault) Wessinghe MBA

Please leave space on the back for book description (one paragraph) and author biography (short paragraph)

```html
<!DOCTYPE html>
<html lang="nl">
<head>
<meta charset="utf-8">
<title>Mr. Dr. Anselm ter Haar Veldt – Boekomslag</title>
<link rel="stylesheet" href="https://fonts.googleapis.com/css2?family=Oswald:wght@500;700&family=Open+Sans:wght@400;600&family=Merriweather:wght@700&display=swap">
<style>
  :root {
    --stage: #ecebe7;
    --sepia-light: #b3ad9b;
    --sepia-mid: #8f8877;
    --sepia-dark: #5e5747;
    --back-light: #7a624b;
    --back-dark: #3f3123;
    --ink: #2a2420;
    --ink-red: #5a1f14;
    --paper: #f4efe6;
    --band: rgba(240, 234, 222, 0.55);
    --back-band: rgba(40, 30, 20, 0.55);
  }
  * { box-sizing: border-box; margin: 0; padding: 0; }
  html, body { width: 1200px; height: 1000px; overflow: hidden; background: var(--stage); }
  .cover-wrap {
    position: absolute; left: 52px; top: 110px;
    width: 1096px; height: 780px;
    display: flex;
    box-shadow: 0 10px 30px rgba(0,0,0,0.25);
  }

  /* Back cover */
  .back {
    position: relative; width: 520px; height: 100%; overflow: hidden;
    color: var(--paper);
  }
  .back-photo {
    position: absolute; inset: 0;
    background: linear-gradient(160deg, var(--back-light) 0%, #6b5440 45%, var(--back-dark) 100%);
  }
  .back-inset-photo {
    position: absolute; left: 140px; top: 70px; width: 120px; height: 130px;
    background: linear-gradient(170deg, #e4e0d8, #8c877e 60%, #3b3834);
    border: 4px solid var(--paper);
  }
  .back-description {
    position: absolute; left: 34px; top: 230px; width: 450px;
    font: 400 9.5px/1.5 "Open Sans", sans-serif; color: rgba(244,239,230,0.9);
  }
  .back-quote-mark {
    position: absolute; left: 196px; top: 300px;
    font: 700 46px/1 "Merriweather", serif; color: var(--paper);
  }
  .back-quote {
    position: absolute; left: 226px; top: 320px; width: 250px;
    font: 700 13px/1.45 "Merriweather", serif; color: var(--paper);
  }
  .back-author-bio {
    position: absolute; left: 226px; top: 530px; width: 250px;
    font: 700 11px/1.45 "Merriweather", serif; color: rgba(244,239,230,0.9);
  }
  .back-publisher-band {
    position: absolute; left: 0; right: 0; bottom: 40px; height: 62px;
    background: var(--back-band);
    display: flex; align-items: center; padding-left: 36px;
    font: 600 12px/1 "Open Sans", sans-serif; letter-spacing: 0.35em; color: var(--paper);
  }

  /* Spine */
  .spine {
    position: relative; width: 56px; height: 100%; overflow: hidden;
    background: linear-gradient(180deg, var(--sepia-light), var(--sepia-mid));
    border-left: 1px solid rgba(0,0,0,0.15); border-right: 1px solid rgba(0,0,0,0.15);
    display: flex; flex-direction: column; align-items: center; padding: 26px 0;
  }
  .spine-title, .spine-author { writing-mode: vertical-rl; white-space: nowrap; }
  .spine-title { font: 700 27px/1 "Oswald", sans-serif; color: var(--ink); letter-spacing: 0.01em; }
  .spine-author {
    margin-top: auto; font: 600 11px/1 "Open Sans", sans-serif; letter-spacing: 0.25em; color: var(--ink);
  }

  /* Front cover */
  .front { position: relative; width: 520px; height: 100%; overflow: hidden; text-align: center; }
  .front-photo {
    position: absolute; inset: 0;
    background:
      radial-gradient(ellipse at 40% 60%, #7c7565 0%, transparent 55%),
      linear-gradient(180deg, #c3bdab 0%, var(--sepia-light) 30%, var(--sepia-mid) 70%, var(--sepia-dark) 100%);
  }
  .front-intro {
    position: relative; margin: 46px auto 0; width: 360px;
    font: 400 13px/1.35 "Open Sans", sans-serif; color: var(--ink);
  }
  .front-title {
    position: relative; margin-top: 22px;
    font: 700 31px/1.1 "Oswald", sans-serif; color: var(--ink); text-transform: uppercase;
  }
  .front-subtitle {
    position: relative; margin-top: 12px;
    font: 500 19px/1.2 "Oswald", sans-serif; color: var(--ink-red); text-transform: uppercase;
  }
  .front-author-band {
    position: absolute; left: 0; right: 0; bottom: 36px; height: 60px;
    background: var(--band);
    display: flex; align-items: center; justify-content: center;
    font: 600 15px/1 "Open Sans", sans-serif; color: var(--ink);
  }
</style>
</head>
<body>
  <div class="cover-wrap">
    <section class="back">
      <div class="back-photo" role="img" aria-label="Vervaagde sepiafoto van de politicus in pak, achtergrond van de achterzijde"></div>
      <div class="back-inset-photo" role="img" aria-label="Kleine zwart-witfoto van de politicus tussen een groep mensen"></div>
      <p class="back-description">Deze politieke biografie volgt het leven van een jurist die de eilanden een eigen stem gaf. Van zijn studiejaren tot de ronde tafel beschrijft het boek zijn strijd voor zelfbestuur, zijn tegenstanders en zijn blijvende invloed op het bestuur van de westelijke eilanden.</p>
      <span class="back-quote-mark">&ldquo;</span>
      <p class="back-quote">Een helder en zorgvuldig portret van een man die het politieke landschap van zijn tijd veranderde. Wessinghe combineert archiefwerk met persoonlijke getuigenissen en laat zien hoe vastberaden idealen uitgroeiden tot een nieuwe staatkundige orde.</p>
      <p class="back-author-bio">drs. K.J. (Thibault) Wessinghe MBA is econoom en schrijver. Hij doceerde bestuurskunde en publiceert over de geschiedenis van de eilanden.</p>
      <div class="back-publisher-band">UITGEVERIJ KLEINE BAAI</div>
    </section>

    <section class="spine">
      <span class="spine-title">MR. DR. ANSELM TER HAAR VELDT</span>
      <span class="spine-author">drs. K.J. (Thibault) Wessinghe MBA</span>
    </section>

    <section class="front">
      <div class="front-photo" role="img" aria-label="Sepiafoto van de politicus in pak met stropdas, pratend aan tafel"></div>
      <p class="front-intro">This book is a political biography of Mr. Ter Haar Veldt who was a prominent politician in Curacao.</p>
      <h1 class="front-title">Mr. Dr. Anselm ter Haar Veldt:</h1>
      <h2 class="front-subtitle">Pionier voor het Bestuurlijke Zelfbeschikking<br>der Westelijke Eilanden</h2>
      <div class="front-author-band">drs. K.J. (Thibault) Wessinghe MBA</div>
    </section>
  </div>
</body>
</html>
```